Corporate-Design für Altreifenentsorgung/Container
Zielgruppe
Wir sind ein Familienunternehmen das zum Jahreswechsel vom Gründer Ferdinand Wunsiedl an seinen Sohn Thomas Wunsiedl übergeben wurde. Also Inhabergeführtes Familienunternehmen ist uns der persönliche Kontakt mit den Kunden sehr wichtig. Gemeinsam versuchen wir immer eine Individuelle Lösung zu finden um den Anforderungen der Kunden exakt entsprechen.
Wir betreiben drei Geschäftsbereiche:
- Heu & Stroh : Wir beliefern Landwirte, Reitställe, Tierparks, usw. ganzjährig mit hochwertigem Heu, Stroh, und anderen Futtermittel auch in Bio-Qualität. Die Lieferung zu den Kunden in Deutschland, Österreich, Italien und der Schweiz erfolgt mit eigenen LKWs
- Altreifenentsorgung: Wir entsorgen alle Arten von Altreifen von KFZ/LKW-Werkstätten, Speditionen, landwirtschaftlichen Betrieben, Bauunternehmen, usw.... Die Reifen werden von uns direkt beim Kunden abgeholt und einer Fach- und Umweltgerechten Verwertung zugeführt.
- Container: Unser jüngster Geschäftsbereich. Wir vertreiben neue und gebrauchte Abrollcontainer für den Transport und zur Lagerung von Schotter, Abfällen, Baumaschinen, Baustoffen, usw. Besonderheit hierbei ist, dass wir einen großen Lagerbestand an neuen und gebrauchten Containern haben. Somit können sich unsere Kunden sofort verfügbare Modelle ohne Lieferzeit aussuchen und sofort einsetzen. Außerdem vermieten wir diese Container auch (Containerdienst)
weitere Information finden Sie unter www.ferdinand-wunsiedl.de
Aufgabenstellung
Wir wünschen uns ein Zeitgemäßes Logo in dem man jedoch erkennen kann die' Verwandtschaft' zur alten Firma erkennen kann. So sollten sich die Farben gelb und grün im neuen Logo wiederfinden.
Der Slogan 'Natürlich. Zuverlässig. Handeln.' sollte im Logo enthalten sein
Die Geschäftsbereiche 'Heu & Stroh - Altreifenentsorgung - Container' können, müssen aber nicht im Logo erwähnt werden. Falls sie jedoch nicht im Logo erwähnt werden, sollten Sie jedoch auf Briefpapier und Visitenkarten gedruckt werden.
Auf der Visitenkarte sollte eine V-Card als QR-Code abgebildet sein.
Weitere Daten für Visitenkarte:
Name: Thomas Wunsiedl
Adresse: Kastanienweg 17, 85599 Pöringhof
Tel: +49 89-7712058
Fax: +49 89-7719058
Mob: +49 152-06137482
web: www.wunsiedl.bayern
e-mail: wird nachgereicht
zusätzliche Angaben auf Briefpapier:
Bank: Raiffeisenkasse Kelbachtal eG
IBAN: DE41 7021 3357 0004 6215 80
BIC: GENO DEF1 KBT
Öko-Kontrollstellennummer: DE-ÖKO-091
UID: wird nachgereicht
Steuer-Nr.: wird nachgereicht

```html
<!DOCTYPE html>
<html lang="de">
<head>
<meta charset="utf-8">
<title>Visitenkarte – Thomas Wunsiedl</title>
<link rel="stylesheet" href="https://fonts.googleapis.com/css2?family=Montserrat:wght@400;600;700&display=swap">
<style>
  :root {
    --bg: #e6e6e6;
    --green: #6cb33f;
    --green-dark: #5a9e33;
    --yellow: #f2d11b;
    --paper: #fbfbf9;
    --ink: #3a3a3a;
    --ink-soft: #555555;
    --white: #ffffff;
  }
  * { box-sizing: border-box; margin: 0; padding: 0; }
  html, body {
    width: 1200px;
    height: 898px;
    overflow: hidden;
    background: var(--bg);
    font-family: "Montserrat", sans-serif;
  }
  .stage {
    width: 1200px;
    height: 898px;
    display: flex;
    align-items: center;
    justify-content: center;
    gap: 60px;
  }
  .card {
    width: 530px;
    height: 343px;
    position: relative;
    box-shadow: 0 6px 18px rgba(0,0,0,0.12);
  }
  .card--back {
    background: var(--green);
    display: flex;
    flex-direction: column;
    align-items: center;
    justify-content: center;
    color: var(--white);
  }
  .brand-mark {
    width: 34px;
    height: 34px;
    background: var(--white);
    margin-bottom: 16px;
  }
  .brand-name {
    font-weight: 600;
    font-size: 30px;
    letter-spacing: 0.5px;
  }
  .brand-slogan {
    margin-top: 6px;
    font-size: 12px;
    font-weight: 400;
    letter-spacing: 0.6px;
  }
  .card--front {
    background: var(--paper);
    color: var(--ink);
  }
  .front-brand {
    position: absolute;
    left: 48px;
    top: 138px;
    display: flex;
    align-items: center;
    gap: 14px;
  }
  .front-brand__square {
    width: 46px;
    height: 46px;
    background: var(--yellow);
  }
  .front-brand__name {
    font-weight: 700;
    font-size: 30px;
    color: var(--green);
  }
  .contact {
    position: absolute;
    left: 300px;
    top: 62px;
  }
  .contact__name {
    font-weight: 600;
    font-size: 19px;
    color: var(--ink);
    margin-bottom: 12px;
  }
  .contact__list {
    list-style: none;
    font-size: 10.5px;
    line-height: 1.75;
    color: var(--ink-soft);
  }
</style>
</head>
<body>
  <main class="stage">
    <section class="card card--back" aria-label="Visitenkarte Rückseite">
      <div class="brand-mark" aria-hidden="true"></div>
      <div class="brand-name">Thomas Wunsiedl</div>
      <div class="brand-slogan">Natürlich. Zuverlässig. Handeln.</div>
    </section>

    <section class="card card--front" aria-label="Visitenkarte Vorderseite">
      <div class="front-brand">
        <div class="front-brand__square" aria-hidden="true"></div>
        <div class="front-brand__name">Wunsiedl</div>
      </div>
      <div class="contact">
        <h1 class="contact__name">Thomas Wunsiedl</h1>
        <ul class="contact__list">
          <li>Kastanienweg 17, 85599 Pöringhof</li>
          <li>Tel.: +49 89-7712058</li>
          <li>Fax: +49 89-7719058</li>
          <li>Mobil: +49 152-06137482</li>
          <li>web: www.wunsiedl.bayern</li>
        </ul>
      </div>
    </section>
  </main>
</body>
</html>
```